K7 Maplewave Consulting Group Ltd - Website Design

We already have a company logo. We need a website created for our consulting agency.
Refer to attached files for logo and website content.
We would also be open to any additional recommendations.
Industry/Entity Type
Finance And Accounting
Coding
Coded - Design and coding required
Number of Pages Required
1 page
Font styles to use
Serif
Colors
3377b5
b868aa
33b8a4
Requirements
Must have
- Company Logo, name and who we are.

```html
<!DOCTYPE html>
<html lang="en">
<head>
<meta charset="utf-8">
<title>K7 Maplewave Consulting Group Ltd</title>
<link rel="stylesheet" href="https://fonts.googleapis.com/css2?family=Jost:wght@300;400;500;600&family=Lora:wght@500;600&display=swap">
<style>
:root{
  --navy:#2a1d78;
  --navy-deep:#221867;
  --ink:#2b2562;
  --text:#5b5b70;
  --muted:#8a8a99;
  --hero-bg:#eef1f6;
  --soft:#f4f5f9;
  --line:#c9c9d6;
  --white:#ffffff;
  --brand-blue:#3377b5;
  --brand-rose:#b868aa;
  --brand-teal:#33b8a4;
}
*{margin:0;padding:0;box-sizing:border-box}
html,body{width:1200px;height:4383px;overflow:hidden}
body{position:relative;background:var(--white);font-family:"Jost",sans-serif;color:var(--ink)}
.abs{position:absolute}
.serif{font-family:"Lora",serif}
.btn{position:absolute;display:flex;align-items:center;justify-content:center;border-radius:26px;font-size:18px;font-weight:400}
.btn--dark{background:var(--navy);color:var(--white)}
.btn--light{background:var(--white);color:var(--navy)}
.btn--outline{border:2px solid var(--navy);color:var(--navy);background:var(--white)}

/* header */
.brand{left:48px;top:40px;font-size:28px;font-weight:400;color:var(--navy);line-height:1}
.brand small{display:block;font-family:"Jost",sans-serif;font-size:9px;font-weight:500;letter-spacing:.5px;margin-top:6px}
.nav{left:565px;top:45px;display:flex;gap:34px;font-size:21px;color:var(--white)}
.nav-cta{left:950px;top:37px;width:199px;height:43px;font-size:20px}

/* hero */
.hero-title{left:68px;top:226px;font-size:46px;font-weight:500;color:#1a1540}
.hero-sub{left:68px;top:290px;font-size:29px;font-weight:500;color:#1a1540}
.hero-text{left:68px;top:355px;font-size:20px;line-height:31px;color:var(--ink);font-weight:500}
.hero-btn{left:72px;top:463px;width:197px;height:49px}
.mouse{left:590px;top:576px;width:20px;height:34px;border:2px solid #a7abbd;border-radius:10px}

/* about */
.about-frame{left:208px;top:786px;width:412px;height:365px;border:4px solid var(--navy);border-radius:10px}
.about-photo{left:148px;top:761px;width:436px;height:354px;border:6px solid var(--white);border-radius:10px;box-shadow:0 6px 20px rgba(30,30,80,.18);background:linear-gradient(135deg,#3d4a63,#6f8fb3 55%,#e7e9ee)}
.name-tag{font-size:17px;font-weight:500;color:var(--navy);display:flex;align-items:center;gap:8px}
.name-tag i{display:block;width:12px;height:12px;border-radius:50%;background:var(--brand-teal)}
.about-tag{left:706px;top:815px}
.about-title{left:706px;top:866px;font-size:42px;font-weight:600;color:var(--navy)}
.about-text{left:706px;top:936px;width:365px;font-size:15px;line-height:24px;color:var(--text)}

/* services */
.svc-tag{left:0;width:1200px;top:1270px;justify-content:center}
.svc-kicker{left:0;width:1200px;top:1314px;text-align:center;font-size:32px;color:var(--muted)}
.svc-title{left:0;width:1200px;top:1358px;text-align:center;font-size:42px;font-weight:600;color:var(--navy)}
.card{position:absolute;width:296px;background:var(--white);border:1px solid #e2e2ea;border-radius:6px;box-shadow:0 4px 14px rgba(40,40,90,.08);padding:0 29px}
.card svg{position:absolute;left:29px;top:32px}
.card h3{position:absolute;left:29px;font-size:18px;font-weight:500;color:var(--navy)}
.card p{position:absolute;left:29px;width:230px;font-size:16px;line-height:20px;color:var(--text)}
.card--active{background:var(--navy);border-color:var(--navy)}
.card--active h3,.card--active p{color:var(--white)}
.svc-btn{left:500px;top:2109px;width:198px;height:51px}

/* cta */
.cta-plane{left:128px;top:2374px;width:408px;height:281px;border-radius:50%;background:radial-gradient(circle,#3a2e91 0,#2f2384 55%,rgba(42,29,120,0) 72%)}
.cta-photo{left:930px;top:2270px;width:200px;height:555px;background:linear-gradient(180deg,rgba(184,104,170,.25),rgba(51,119,181,.25))}
.cta-kicker{left:557px;top:2400px;font-size:33px;font-weight:300;color:#c7c3e6}
.cta-title{left:557px;top:2448px;font-size:42px;font-weight:600;line-height:54px;color:var(--white)}
.cta-btn{left:558px;top:2599px;width:198px;height:49px}

/* blog */
.blog-title{left:0;width:1200px;top:2870px;text-align:center;font-size:44px;font-weight:300;color:var(--navy)}
.blog-title b,.touch-title b{font-family:"Lora",serif;font-weight:600}
.post{position:absolute;top:2975px;width:287px;height:381px;background:var(--white);border-radius:6px;box-shadow:0 4px 14px rgba(40,40,90,.1);overflow:hidden}
.post-img{height:174px}
.post-body{padding:24px 23px 0}
.post-by{font-size:12px;color:var(--muted)}
.post-head{margin-top:8px;font-size:18px;line-height:22px;font-weight:400;color:var(--ink)}
.post-text{margin-top:6px;font-size:14px;line-height:19px;color:var(--muted)}
.post-more{display:block;margin-top:9px;font-size:14px;color:var(--navy);text-decoration:underline}
.blog-btn{left:500px;top:3397px;width:198px;height:50px}

/* contact */
.touch-title{left:0;width:1200px;top:3606px;text-align:center;font-size:44px;font-weight:300;color:var(--navy)}
.field{position:absolute;border:2px solid var(--line);background:var(--white);font-size:18px;color:var(--text);padding:8px 16px}
.touch-btn{left:516px;top:3923px;width:167px;height:48px;font-size:20px}

/* footer */
.footer{left:0;top:4037px;width:1200px;height:346px;background:var(--navy-deep)}
.foot-logo{left:131px;top:4100px;width:216px;height:131px;background:var(--white);border-radius:8px;display:flex;flex-direction:column;align-items:center;justify-content:center;color:var(--navy);font-size:24px}
.foot-logo small{font-family:"Jost",sans-serif;font-size:8px;font-weight:500;margin-top:4px}
.foot-head{font-size:21px;font-weight:400;color:var(--white)}
.foot-links{left:473px;top:4143px;list-style:none;font-size:13px;line-height:29px;color:#cfcbea}
.foot-links li:before{content:"›";margin-right:8px}
.foot-note{left:722px;top:4128px;font-size:14px;color:#cfcbea}
.sub-form{left:722px;top:4165px;width:345px;height:37px;border-radius:19px;overflow:hidden;display:flex;border:1px solid var(--white)}
.sub-form span{flex:1;background:var(--white);color:var(--muted);font-size:14px;padding:9px 22px}
.sub-form b{width:126px;background:var(--navy-deep);color:var(--white);font-weight:400;font-size:16px;display:flex;align-items:center;justify-content:center}
.social{position:absolute;top:4243px;width:34px;height:34px;border:2px solid var(--white);border-radius:50%}
.copy{left:0;width:1200px;top:4342px;text-align:center;font-size:14px;color:#cfcbea}
</style>
</head>
<body>

<svg class="abs" style="left:0;top:0" width="1200" height="1240" viewBox="0 0 1200 1240">
  <path d="M0 0H1200V1160C1080 1215 960 1240 760 1215C500 1185 250 1160 0 1170Z" fill="#eef1f6"/>
  <path d="M360 0C470 120 430 300 520 420C620 540 900 620 1200 620V0Z" fill="#e1e5ee"/>
</svg>
<svg class="abs" style="left:560px;top:0" width="640" height="660" viewBox="0 0 640 660" role="img" aria-label="Photo of two businessmen in a meeting at a laptop">
  <defs><linearGradient id="heroPhoto" x1="0" y1="0" x2="1" y2="1"><stop offset="0" stop-color="#3b4a6a"/><stop offset=".5" stop-color="#9b8e86"/><stop offset="1" stop-color="#d9dbe2"/></linearGradient></defs>
  <path d="M0 0H640V612C520 640 330 610 230 520C130 430 140 250 70 130C45 80 20 40 0 0Z" fill="url(#heroPhoto)"/>
</svg>

<header>
  <div class="abs brand serif">K7 Maplewave<small>CONSULTING GROUP LTD</small></div>
  <nav class="abs nav"><span>Home</span><span>About</span><span>Services ⌄</span><span>Blog</span></nav>
  <a class="btn btn--light nav-cta">Contact with Us</a>
</header>

<section>
  <h1 class="abs hero-title serif">Financial Planners</h1>
  <p class="abs hero-sub">We help business innovate and grow</p>
  <p class="abs hero-text">Specialized services for small and<br>medium sized enterprises</p>
  <a class="btn btn--dark hero-btn">Learn More</a>
  <div class="abs mouse"></div>
</section>

<section>
  <div class="abs about-frame"></div>
  <div class="abs about-photo" role="img" aria-label="Photo of a hand over a tablet showing financial charts"></div>
  <div class="abs name-tag about-tag"><i></i>K7 Maplewave</div>
  <h2 class="abs about-title serif">About K7 Maplewave</h2>
  <p class="abs about-text">Lorem Ipsum is simply dummy text of the printing and typesetting industry. Lorem Ipsum has been the industry's standard dummy text ever since the 1500s, when an unknown printer took a galley of type and scrambled it to make a type specimen book. Lorem Ipsum has been the</p>
</section>

<section>
  <div class="abs name-tag svc-tag"><i></i>K7 Maplewave</div>
  <p class="abs svc-kicker">What we do</p>
  <h2 class="abs svc-title serif">Services Offered?</h2>

  <div class="card" style="left:133px;top:1503px;height:250px">
    <svg width="60" height="60" viewBox="0 0 60 60" fill="none" stroke="#2a1d78" stroke-width="2"><circle cx="44" cy="38" r="14" fill="#dce9f5" stroke="none"/><rect x="4" y="6" width="30" height="46" rx="2"/><rect x="9" y="11" width="20" height="9"/><path d="M9 27h20M9 34h20M9 41h20M16 24v24M23 24v24"/><rect x="37" y="4" width="10" height="46" rx="2"/></svg>
    <h3 style="top:117px">Accounting</h3>
    <p style="top:148px">Lorem Ipsum is simply dummy text of the printing</p>
  </div>
  <div class="card card--active" style="left:451px;top:1462px;height:252px">
    <svg width="60" height="60" viewBox="0 0 60 60" fill="none" stroke="#fff" stroke-width="2"><circle cx="46" cy="30" r="14" fill="#3b2f8c" stroke="none"/><rect x="4" y="6" width="48" height="34" rx="3"/><rect x="9" y="11" width="38" height="24"/><path d="M24 18l-4 5 4 5M32 18l4 5-4 5M30 16l-4 14M22 40v8M34 40v8M16 48h24"/></svg>
    <h3 style="top:134px">Bookkeeping</h3>
    <p style="top:166px">Lorem Ipsum is simply dummy text of the printing</p>
  </div>
  <div class="card" style="left:771px;top:1503px;height:250px">
    <svg width="66" height="60" viewBox="0 0 66 60" fill="none" stroke="#2a1d78" stroke-width="2"><circle cx="46" cy="30" r="15" fill="#f1e1ee" stroke="none"/><circle cx="33" cy="12" r="6"/><circle cx="18" cy="18" r="5"/><circle cx="48" cy="18" r="5"/><path d="M8 36l12-8 10 6 6-2 14-4 10 8M20 40l10 8 14-10"/></svg>
    <h3 style="top:127px">Financial Management</h3>
    <p style="top:158px">Lorem Ipsum is simply dummy text of the printing</p>
  </div>
  <div class="card" style="left:133px;top:1780px;height:250px">
    <svg width="60" height="60" viewBox="0 0 60 60" fill="none" stroke="#2a1d78" stroke-width="2"><circle cx="44" cy="32" r="14" fill="#daf1ed" stroke="none"/><rect x="4" y="4" width="36" height="44" rx="4"/><path d="M11 14h22M11 22h22M11 30h14M28 44l6 6 12-14"/></svg>
    <h3 style="top:130px">Government Grants</h3>
    <p style="top:162px">Lorem Ipsum is simply dummy text of the printing</p>
  </div>
  <div class="card" style="left:451px;top:1739px;height:249px">
    <svg width="60" height="60" viewBox="0 0 60 60" fill="none" stroke="#2a1d78" stroke-width="2"><circle cx="46" cy="34" r="14" fill="#dce9f5" stroke="none"/><rect x="22" y="20" width="12" height="12"/><circle cx="10" cy="10" r="5"/><circle cx="46" cy="10" r="5"/><circle cx="10" cy="44" r="5"/><circle cx="46" cy="44" r="5"/><circle cx="28" cy="6" r="4"/><circle cx="28" cy="48" r="4"/><path d="M14 14l8 8M42 14l-8 8M14 40l8-8M42 40l-8-8M28 10v10M28 32v12"/></svg>
    <h3 style="top:130px">Strategy</h3>
    <p style="top:161px">Lorem Ipsum is simply dummy text of the printing</p>
  </div>
  <div class="card" style="left:771px;top:1780px;height:250px">
    <svg width="66" height="60" viewBox="0 0 66 60" fill="none" stroke="#2a1d78" stroke-width="2"><circle cx="48" cy="32" r="14" fill="#f1e1ee" stroke="none"/><rect x="4" y="6" width="54" height="36" rx="3"/><rect x="11" y="12" width="10" height="7"/><rect x="25" y="12" width="10" height="7"/><rect x="39" y="12" width="10" height="7"/><path d="M11 26h38M11 32h38M24 42v8M38 42v8M18 50h26"/></svg>
    <h3 style="top:127px">Mergers and Acquisitions</h3>
    <p style="top:158px">Lorem Ipsum is simply dummy text of the printing</p>
  </div>

  <a class="btn btn--dark svc-btn">All Services</a>
</section>

<svg class="abs" style="left:0;top:2140px" width="1200" height="645" viewBox="0 0 1200 645">
  <path d="M0 10C120 40 300 200 560 170C820 140 1000 60 1200 75V645H0Z" fill="#2a1d78"/>
</svg>
<section>
  <div class="abs cta-plane" role="img" aria-label="Illustration of a paper plane flying from concentric circles"></div>
  <div class="abs cta-photo" role="img" aria-label="Cut-out photo of a smiling woman holding a phone"></div>
  <p class="abs cta-kicker">Change starts here</p>
  <h2 class="abs cta-title serif">Take your first step<br>towards RESULT.</h2>
  <a class="btn btn--light cta-btn">Email us Today</a>
</section>

<svg class="abs" style="left:0;top:2783px" width="1200" height="740" viewBox="0 0 1200 740">
  <path d="M0 0H1200V690C1000 730 800 700 600 700C400 700 200 740 0 720Z" fill="#f4f5f9"/>
</svg>
<section>
  <h2 class="abs blog-title">Latest <b>Blog</b></h2>
  <article class="post" style="left:133px">
    <div class="post-img" role="img" aria-label="Photo of a laptop lit by pink and blue light" style="background:linear-gradient(135deg,#b868aa,#3377b5 55%,#1d2a6b)"></div>
    <div class="post-body"><p class="post-by">By Admin</p><h3 class="post-head">Lorem Ipsum is simply dummy text of the printing</h3><p class="post-text">There are many variations of passages of available but majority have alteration</p><a class="post-more">Read More</a></div>
  </article>
  <article class="post" style="left:456px">
    <div class="post-img" role="img" aria-label="Photo of a businessman holding a tablet with digital charts" style="background:linear-gradient(135deg,#a9c6dc,#3377b5 50%,#1b2437)"></div>
    <div class="post-body"><p class="post-by">By Admin</p><h3 class="post-head">Lorem Ipsum is simply dummy text of the printing</h3><p class="post-text">There are many variations of passages of available but majority have alteration</p><a class="post-more">Read More</a></div>
  </article>
  <article class="post" style="left:780px">
    <div class="post-img" role="img" aria-label="Photo of a man in a suit writing at an office desk" style="background:linear-gradient(135deg,#dfe4e6,#8d9297 55%,#3b3f46)"></div>
    <div class="post-body"><p class="post-by">By Admin</p><h3 class="post-head">Lorem Ipsum is simply dummy text of the printing</h3><p class="post-text">There are many variations of passages of available but majority have alteration</p><a class="post-more">Read More</a></div>
  </article>
  <a class="btn btn--dark blog-btn">View all Blogs</a>
</section>

<section>
  <h2 class="abs touch-title">Get In <b>Touch</b></h2>
  <div class="field" style="left:272px;top:3697px;width:315px;height:44px">Your Name</div>
  <div class="field" style="left:272px;top:3768px;width:315px;height:45px">Email</div>
  <div class="field" style="left:272px;top:3840px;width:315px;height:46px">Phone</div>
  <div class="field" style="left:611px;top:3697px;width:315px;height:189px">Message</div>
  <a class="btn btn--outline touch-btn">Email us</a>
</section>

<footer>
  <div class="abs footer"></div>
  <div class="abs foot-logo serif">K7 Maplewave<small>CONSULTING GROUP LTD</small></div>
  <h4 class="abs foot-head" style="left:473px;top:4093px">COMPANY</h4>
  <ul class="abs foot-links"><li>Home</li><li>About Us</li><li>Services</li><li>Blog</li><li>Contact Us</li></ul>
  <h4 class="abs foot-head" style="left:722px;top:4088px">SUBSCRIBE</h4>
  <p class="abs foot-note">Subscribe to newsletter</p>
  <div class="abs sub-form"><span>Email address</span><b>Subscribe</b></div>
  <span class="social" style="left:723px"></span>
  <span class="social" style="left:766px"></span>
  <span class="social" style="left:809px"></span>
  <span class="social" style="left:852px"></span>
  <p class="abs copy">© 2021 K7 Maplewave. All Rights Reserved.</p>
</footer>

</body>
</html>
```